Sponsored Fundraiser Needs Flyer

We need a flyer for a law firm sponsored fundraiser and community event. Pellmark Law Group is looking to become a familiar company for our community, and is hosting an Easter Egg Hunt & Yard Sale Fundraiser to raise money for the Miss Brightfield Service Pageant. See attached generic template for basic information.

Target Market(s)

Local Community

Industry/Entity Type

Community

Font styles to use
Decorative

Requirements
Must have
• Sponsorship information, fundraiser information, location information, website for fundraiser payments, logo for fundraiser group, logo for law group
Nice to have
• Colorful and inviting feel, eye catching designs

```html
<!DOCTYPE html>
<html lang="en">
<head>
<meta charset="utf-8">
<title>Easter Egg Hunt &amp; Yard Sale Fundraiser</title>
<link rel="stylesheet" href="https://fonts.googleapis.com/css2?family=Fredoka:wght@500;600;700&family=Open+Sans:wght@400;600;700&display=swap">
<style>
:root{
  --orange:#f15a29;
  --orange-light:#f7a15c;
  --green:#3bb54a;
  --red:#d81f26;
  --red-dark:#a51c22;
  --white:#ffffff;
  --ink:#1a1a1a;
  --peach:#fde3cf;
  --navy:#23395d;
}
*{box-sizing:border-box;margin:0;padding:0}
html,body{width:848px;height:1200px;overflow:hidden}
body{background:var(--orange);font-family:"Open Sans",Arial,sans-serif;color:var(--ink);position:relative}
.sponsor-band{position:absolute;left:18px;top:18px;width:66px;height:1164px;background:linear-gradient(90deg,var(--peach),#fff3ea);overflow:hidden}
.sponsor-note{position:absolute;left:58px;top:8px;transform-origin:0 0;transform:rotate(90deg);width:690px;font-size:14px;line-height:18px;color:var(--ink)}
.sponsor-name{position:absolute;left:0;top:996px;width:66px;height:160px}
.sponsor-name i{position:absolute;left:22px;top:0;width:26px;height:26px;background:var(--navy)}
.sponsor-name span{position:absolute;left:52px;top:34px;transform-origin:0 0;transform:rotate(90deg);white-space:nowrap;font-size:16px;line-height:19px;letter-spacing:1px;text-transform:uppercase;color:var(--ink)}
.ribbon{position:absolute;left:86px;top:18px;width:60px;height:1164px;background:linear-gradient(90deg,var(--red-dark),var(--red) 40%,#ef3b3b 60%,var(--red-dark))}
.panel{position:absolute;left:148px;top:18px;width:682px;height:1164px;background:var(--white);overflow:hidden}
.title{font-family:"Fredoka",sans-serif;font-weight:700;text-align:center;text-transform:uppercase;letter-spacing:2px;line-height:44px;padding-top:14px}
.title .l1{color:var(--orange);font-size:40px}
.title .l2{color:var(--green);font-size:41px}
.photo{position:absolute;left:0;top:120px;width:682px;height:180px;background:linear-gradient(180deg,#e9e9e9 0%,#d9c34a 30%,#c63a3a 55%,#6ab53a 70%,#3f8f2a 100%)}
.green{position:absolute;left:0;top:278px;width:682px;height:306px}
.green svg{position:absolute;left:0;top:0}
.green-text{position:absolute;left:0;top:72px;width:682px;text-align:center;color:var(--white);font-family:"Fredoka",sans-serif;text-transform:uppercase;letter-spacing:2px;font-weight:500;font-size:12.5px;line-height:22px}
.green-text .venue{font-size:17px;font-weight:600}
.tag{position:absolute;top:212px;width:122px;height:54px;border-radius:8px;border:4px solid var(--white);background:linear-gradient(180deg,var(--orange-light),var(--orange));color:var(--white);font-family:"Fredoka",sans-serif;font-weight:700;font-size:30px;text-align:center;line-height:46px;box-shadow:0 3px 5px rgba(0,0,0,.25)}
.tag.fun{left:180px;transform:rotate(-8deg)}
.tag.prizes{left:420px;width:154px;transform:rotate(6deg)}
.food{position:absolute;left:0;top:282px;width:682px;text-align:center;color:var(--white);font-family:"Fredoka",sans-serif;font-weight:600;font-size:16px;letter-spacing:1.5px;text-transform:uppercase}
.about{position:absolute;left:0;top:608px;width:682px;padding:0 34px;text-align:center;font-size:14px;line-height:18px}
.about p+p{margin-top:8px}
.about .price{color:var(--orange);font-weight:700;font-size:21px}
.details{position:absolute;left:0;top:765px;width:682px;height:233px;background:var(--orange);color:var(--white);text-align:center}
.details h2{font-size:21px;font-weight:700;margin-top:12px;line-height:26px}
.details .addr{font-size:12.5px;margin-top:2px}
.details .times{font-size:18px;font-weight:700;line-height:27px}
.register{position:absolute;left:0;top:998px;width:682px;height:166px}
.pageant{position:absolute;left:40px;top:30px;width:180px;display:flex;align-items:center;gap:8px;color:var(--ink);font-size:13px;font-weight:600;line-height:16px}
.pageant i{flex:none;width:34px;height:34px;border-radius:50%;background:#1f3a7a}
.reg-text{position:absolute;left:246px;top:16px;width:410px;font-size:13.5px;line-height:18.5px}
.reg-text b.url{font-weight:700}
.reg-text .cta{font-size:17px;font-weight:700;margin-top:4px;display:block}
.bow{position:absolute;left:58px;top:775px;width:218px;height:225px;border-radius:48%;background:radial-gradient(circle at 50% 50%,#f0474b,var(--red) 55%,var(--red-dark))}
</style>
</head>
<body>
<aside class="sponsor-band">
  <p class="sponsor-note">Special thanks to Pellmark Law Group for sponsoring the event.<br>Visit www.pellmarklaw-example.com for all of your personal injury, slip and fall, or workers compensation questions.</p>
  <div class="sponsor-name"><i></i><span>Pellmark<br>Law Group</span></div>
</aside>
<div class="ribbon"></div>

<main class="panel">
  <h1 class="title"><span class="l1">Easter Egg Hunt &amp;</span><br><span class="l2">Yard Sale Fundraiser</span></h1>
  <div class="photo" role="img" aria-label="Row of decorated Easter eggs resting in green grass"></div>

  <section class="green">
    <svg width="682" height="306" viewBox="0 0 682 306"><path d="M0 10 Q341 70 682 10 V306 H0 Z" fill="#f15a29"/><path d="M0 16 Q341 74 682 16 V306 H0 Z" fill="#3bb54a"/></svg>
    <div class="green-text">
      Free community Easter egg hunt at<br>
      <span class="venue">The Maple Rail Depot</span><br>
      Yard sale fundraiser vendors welcome.<br>
      Start your spring cleaning and reserve a space!<br>
      Facepainting by Bright Faces
    </div>
    <div class="tag fun">FUN!</div>
    <div class="tag prizes">PRIZES!</div>
    <div class="food">Free hot dogs, hamburgers, chips and drinks!</div>
  </section>

  <section class="about">
    <p>Our Host Marisa is a semi-finalist in the Miss Brightfield Service Pageant and is fundraising to provide our homeless female veterans with finance training, transitional housing, and job acquisition support.</p>
    <p>For this event we are renting out booth spaces to sell your wares. It takes <span class="price">$25</span> a day to provide housing to a veteran, so we are renting booth space for <span class="price">$25</span> for the day. Set up can begin as early as 0800.</p>
  </section>

  <section class="details">
    <h2>Where:</h2>
    <p class="addr">Maple Rail Depot 214 N Birch Way, Alder Falls, AK 99610</p>
    <h2>When:</h2>
    <p class="times">Booth set-up begins at 8:00<br>Face Painting begins at 10:00<br>Egg Hunt begins at 11:00<br>Food will begin being served at 12:00</p>
  </section>

  <section class="register">
    <div class="pageant"><i></i><span>Miss Brightfield Service Pageant</span></div>
    <p class="reg-text">To register for a space please go to:<br>
      <b class="url">https://www.pagelink-example.com/MarisaForBrightfield/</b><br>
      and click on the GiveCircle link. Post your <b>$25</b> donation amount, with your name. This will reserve your space. All proceeds go directly to Homeward Haven Inc.
      <span class="cta">We only have 20 spaces so register now!</span></p>
  </section>
</main>

<div class="bow" role="img" aria-label="Large red gift ribbon bow tied on the vertical ribbon"></div>
</body>
</html>
```